Ember Ridge Clearing postcard ( for direct mailing) and business card design

Design postcards/Business cards
Dale Horvick
Ember Ridge Clearing
482 Copperfern Rd Lewisville,NC 27023
(336) 555-0184 Dale@Emberridgeclearing.example

The postcard will be used for direct mailing to land owners and contractors to advertise our service. Pictures of the process and equipment along with a short summary of what we do. Business card should be contact info and logo.
Updates

The post cards could say something like this: Forestry Mulching machines are capable of clearing land of unwanted trees and brush with limited disturbance to soils or desirable vegetation. Traditional land clearing methods often present an increased risk of erosion by pushing over trees, uprooting the stump and roots, and substantially disturbing soils.In contrast, mulching the vegetation leaves the soil structure intact. The mulched material can be left on the ground and will act as an erosion barrier while returning nutrients back into the soil through decomposition. Over time, grass will naturally grow through the mulch and can be maintained with mowing.

Target Market(s)

Land owners and contractors who need vegetation cleared

Industry/Entity Type

Forestry Mulching

Requirements
Must have
• picture, brief description of service offered, contact info on postcard. Business card should have contact info and logo.
Nice to have
• I like contour lines as a background but I'd like to see other ideas.

```html
<!DOCTYPE html>
<html lang="en">
<head>
<meta charset="utf-8">
<title>Ember Ridge Clearing – Postcard</title>
<link rel="stylesheet" href="https://fonts.googleapis.com/css2?family=Open+Sans:wght@400;700;800&display=swap">
<style>
  :root{
    --page:#f0f0f0;
    --card:#ffffff;
    --forest:#0f4c36;
    --leaf:#1e8a43;
    --mid:#2eaa4a;
    --lime:#8dc63f;
    --line:#d9e6d4;
    --ink:#1b1b1b;
    --paper-text:#ffffff;
  }
  *{box-sizing:border-box;margin:0;padding:0}
  html,body{width:1107px;height:1200px;overflow:hidden;background:var(--page)}
  body{position:relative;font-family:"Open Sans",Arial,sans-serif}
  .card{position:absolute;width:790px;height:465px;background:var(--card);overflow:hidden;box-shadow:4px 5px 6px rgba(0,0,0,.35)}
  .card--front{left:158px;top:115px}
  .card--back{left:158px;top:606px}
  .card svg.shapes{position:absolute;left:0;top:0}
  .brand{position:absolute;left:16px;top:15px;display:flex;align-items:center;gap:8px}
  .brand__mark{width:24px;height:24px;background:var(--leaf)}
  .brand__name{font-weight:800;font-size:15.5px;line-height:16px;letter-spacing:1.2px;color:var(--ink);text-transform:uppercase}
  .front-copy{position:absolute;left:405px;top:184px;width:354px;color:var(--paper-text);font-size:14.3px;line-height:18.6px;text-align:justify;text-align-last:right}
  .front-copy .slant{float:left;width:92px;height:93px;shape-outside:polygon(0 0,100% 0,0 100%)}
  .back-copy{position:absolute;left:20px;top:22px;width:421px;color:var(--paper-text);font-size:14.3px;line-height:18.6px;text-align:justify}
  .back-copy p:first-child{padding-right:78px}
  .stamp{position:absolute;left:649px;top:24px;width:109px;height:129px;border:1.5px solid var(--lime)}
  .address-line{position:absolute;left:510px;width:244px;height:1px;background:var(--ink)}
</style>
</head>
<body>

<section class="card card--front">
  <svg class="shapes" width="790" height="465" viewBox="0 0 790 465">
    <defs>
      <linearGradient id="sky" x1="0" y1="0" x2="1" y2="0">
        <stop offset="0" stop-color="#ffffff"/><stop offset="1" stop-color="#e9eef2"/>
      </linearGradient>
      <linearGradient id="woods" x1="0" y1="0" x2="0" y2="1">
        <stop offset="0" stop-color="#9a9a90"/><stop offset=".45" stop-color="#6e5b45"/><stop offset="1" stop-color="#3b2e22"/>
      </linearGradient>
    </defs>
    <rect width="790" height="78" fill="url(#sky)"/>
    <rect y="78" width="790" height="387" fill="url(#woods)" role="img" aria-label="Photo: tracked skid steer with a forestry mulcher head clearing brush in winter woods"/>
    <polygon points="187,78 265,0 300,0 222,78" fill="var(--leaf)"/>
    <polygon points="222,78 300,0 335,0 257,78" fill="var(--mid)"/>
    <polygon points="257,78 335,0 370,0 292,78" fill="var(--lime)"/>
    <polygon points="422,78 560,78 640,0 790,0 790,148 422,148" fill="var(--lime)"/>
    <polygon points="560,78 640,0 790,0 790,20 650,148 600,148" fill="var(--forest)"/>
    <polygon points="345,465 345,252 455,148 790,148 790,465" fill="var(--leaf)"/>
    <polygon points="362,465 362,262 466,160 790,160 790,465" fill="var(--forest)"/>
    <polyline points="642,2 735,98 669,164 520,164 383,300 383,443 770,443 790,463" fill="none" stroke="var(--line)" stroke-width="1"/>
    <polyline points="452,124 610,124 700,40" fill="none" stroke="var(--mid)" stroke-width="1"/>
  </svg>
  <div class="brand">
    <span class="brand__mark"></span>
    <span class="brand__name">Ember<br>Ridge<br>Clearing</span>
  </div>
  <p class="front-copy"><span class="slant"></span>Forestry Mulching machines are capable of clearing land of unwanted trees and brush with limited disturbance to soils or desirable vegetation. Traditional land clearing methods often present an increased risk of erosion by pushing over trees, uprooting the stump and roots, and substantially disturbing soils. In contrast, mulching the vegetation leaves the soil structure intact. The mulched material can be left on the ground and will act as an erosion barrier while returning nutrients back into the soil through decomposition. Over time, grass will naturally grow through the mulch and can be maintained with mowing.</p>
</section>

<section class="card card--back">
  <svg class="shapes" width="790" height="465" viewBox="0 0 790 465">
    <defs>
      <linearGradient id="p1" x1="0" y1="0" x2="0" y2="1"><stop offset="0" stop-color="#8a8478"/><stop offset="1" stop-color="#5a4a38"/></linearGradient>
      <linearGradient id="p2" x1="0" y1="0" x2="0" y2="1"><stop offset="0" stop-color="#3c4a3a"/><stop offset=".6" stop-color="#5c6a72"/><stop offset="1" stop-color="#9a8462"/></linearGradient>
      <linearGradient id="p3" x1="0" y1="0" x2="0" y2="1"><stop offset="0" stop-color="#8a8a86"/><stop offset=".5" stop-color="#5a5a5c"/><stop offset="1" stop-color="#333538"/></linearGradient>
    </defs>
    <polygon points="372,15 476,94 476,340 420,340 420,15" fill="var(--lime)"/>
    <polygon points="0,0 356,0 459,94 459,361 0,361" fill="var(--forest)"/>
    <polyline points="436,49 459,26 575,26 605,0" fill="none" stroke="var(--forest)" stroke-width="1.3"/>
    <polyline points="10,449 390,449 405,434" fill="none" stroke="var(--leaf)" stroke-width="1.3"/>
    <g>
      <rect x="8" y="257" width="145" height="178" fill="var(--leaf)" stroke="#ffffff" stroke-width="1"/>
      <rect x="16" y="265" width="129" height="162" fill="url(#p1)" role="img" aria-label="Photo: mulcher arm raised among bare trees"/>
      <rect x="158" y="257" width="145" height="178" fill="var(--leaf)" stroke="#ffffff" stroke-width="1"/>
      <rect x="166" y="265" width="129" height="162" fill="url(#p2)" role="img" aria-label="Photo: front view of skid steer with mulching drum"/>
      <rect x="307" y="257" width="144" height="178" fill="var(--leaf)" stroke="#ffffff" stroke-width="1"/>
      <rect x="315" y="265" width="128" height="162" fill="url(#p3)" role="img" aria-label="Photo: tracked loader on a trailer ready for transport"/>
    </g>
  </svg>
  <div class="back-copy">
    <p>Forestry Mulching is especially economical for smaller plots of land or areas with less access. When land needs to be cleared for adding roads, servicing pipelines, or creating recreational spaces in a wooded area, forestry mulching can be a very effective method of clearing spaces.</p>
    <p>Along with making space for planned projects, forestry mulching is also a great way to clear unwanted vegetation to allow more desirable food sources for local wildlife to flourish. Creating access to waterways that have become overgrown and clearing space for animals to gain new breeding grounds are other ways forestry mulching can be helpful.</p>
  </div>
  <div class="stamp"></div>
  <div class="address-line" style="top:239px"></div>
  <div class="address-line" style="top:301px"></div>
  <div class="address-line" style="top:363px"></div>
</section>

</body>
</html>
```